A private security company called "Tavrin Security Services Ltd"

Hello everybody,

We need a web page for a company based in NZ. It is mainly an informative website so it would be wonderful if the designer puts their absolute best into making it a website that I would really appreciate. The website needs to show professionalism and also needs to make our web surfers find the information they need in a click. the company's colour is black and silver, and if those two colours could be integrated into the website it would be absolutely lovely. Please do contact me for any information.

Sincerely,
Dorian Velasko

Industry/Entity Type

Security

```html
<!DOCTYPE html>
<html lang="en">
<head>
<meta charset="utf-8">
<title>Tavrin Security Services Ltd</title>
<link href="https://fonts.googleapis.com/css2?family=Open+Sans:wght@300;400;600;700&display=swap" rel="stylesheet">
<style>
:root{
  --ink:#1a1a1a;
  --steel:#5c5c5c;
  --panel:#ececec;
  --text-soft:#9a9a9a;
  --text-mid:#555;
  --white:#fff;
  --partner-blue:#1f3f9a;
  --partner-grey:#6e6e6e;
}
*{box-sizing:border-box;margin:0;padding:0}
html,body{width:871px;height:1200px;overflow:hidden;background:var(--white)}
body{font-family:'Open Sans',sans-serif;color:var(--text-mid);position:relative}
.page{position:relative;width:871px;height:1200px;overflow:hidden}

.hero{position:absolute;left:0;top:0;width:871px;height:400px;
  background:linear-gradient(90deg,#6f6f6f 0%,#9d9d9d 22%,#3b3b3b 45%,#1c1c1c 70%,#0c0c0c 100%)}
.hero-shade{position:absolute;left:0;top:0;width:871px;height:140px;
  background:linear-gradient(180deg,rgba(0,0,0,.85),rgba(0,0,0,0))}
.brand{position:absolute;left:16px;top:0;width:165px;height:134px;background:var(--white);
  display:flex;align-items:center;justify-content:center;gap:8px}
.brand-mark{width:14px;height:14px;background:var(--ink);flex:none}
.brand-name{font-weight:700;font-size:13px;line-height:1.25;color:var(--ink);text-transform:uppercase;letter-spacing:.5px}
.enquire{position:absolute;left:728px;top:0;width:112px;height:29px;background:#e8e8e8;
  color:#666;font-size:14px;display:flex;align-items:center;justify-content:center}
.nav{position:absolute;top:70px;left:231px;width:623px;display:flex;justify-content:space-between;list-style:none}
.nav li{color:var(--white);font-size:13.5px;padding:2px 7px;white-space:nowrap}
.nav li.active{background:var(--white);color:var(--ink)}
.slider-dots{position:absolute;top:385px;left:378px;display:flex;gap:10px}
.slider-dots span{width:24px;height:3px;background:#777}
.slider-dots span.on{background:#ddd}

.services{position:absolute;top:452px;left:0;width:871px}
.service{position:absolute;width:204px;height:150px;background:var(--panel)}
.service-head{height:34px;background:var(--steel);color:var(--white);font-size:14px;padding:7px 11px;white-space:nowrap}
.service-avatar{position:absolute;right:5px;top:0;width:44px;height:48px;background:#8a8a8a;border-radius:50% 50% 4px 4px}
.service p{font-size:10px;letter-spacing:-.1px;color:var(--text-soft);line-height:1.2;padding:0 8px 0 11px;margin-top:16px}
.service p+p{margin-top:7px}
.readmore{position:absolute;right:12px;bottom:10px;font-size:11px;color:#444}

.welcome{position:absolute;left:16px;top:656px;width:590px}
.welcome h1{font-weight:300;font-size:22px;color:#555;white-space:nowrap}
.welcome h1 strong{font-weight:400;color:var(--ink)}
.welcome p{font-size:10px;color:var(--text-soft);line-height:1.2;margin:22px 0 0 8px;width:575px}
.welcome p+p{margin-top:12px}

.updates{position:absolute;left:623px;top:658px;width:215px;height:320px;background:var(--white);
  box-shadow:-8px 0 18px rgba(0,0,0,.12)}
.updates-tab{position:absolute;left:39px;top:-3px;width:129px;height:29px;background:var(--panel);
  font-size:16px;color:#666;display:flex;align-items:center;justify-content:center;white-space:nowrap}
.updates-tab:after{content:"";position:absolute;left:52px;top:29px;border:12px solid transparent;border-top:10px solid var(--panel)}
.news{position:absolute;left:18px;width:192px}
.news h3{font-size:11px;font-weight:400;color:#444}
.news p{font-size:10px;letter-spacing:-.1px;color:var(--text-soft);line-height:1.2;margin-top:5px}
.news-rule{position:absolute;left:50px;width:120px;height:1px;background:#ccc}

.partners-label{position:absolute;left:17px;top:907px;font-size:10px;color:#666;letter-spacing:.3px}
.partners{position:absolute;left:0;top:930px;width:600px;height:70px}
.partner{position:absolute;top:4px;width:74px;height:52px}
.partner.box{background:var(--partner-blue);border-right:34px solid var(--partner-grey)}
.partner.blade{background:#2a2a2a;border-radius:50%;width:60px;height:52px}

.footer{position:absolute;left:0;top:1066px;width:871px;height:134px;
  background:linear-gradient(180deg,#000 0%,#2a2a2a 55%,#0e0e0e 100%)}
.foot-col{position:absolute;top:27px;list-style:none}
.foot-col li{font-size:10.5px;color:#eee;line-height:19px;white-space:nowrap}
.follow{position:absolute;left:773px;top:2px;width:71px;height:25px;background:var(--white);
  color:var(--ink);font-size:13px;display:flex;align-items:center;justify-content:center}
.social{position:absolute;top:36px;width:21px;height:21px;border-radius:50%;background:var(--white)}
.copyright{position:absolute;left:0;bottom:2px;width:871px;text-align:center;font-size:8.5px;color:#ddd}
</style>
</head>
<body>
<div class="page">

  <header>
    <div class="hero" role="img" aria-label="Photograph of a security officer in a black shirt beside a model of city towers"></div>
    <div class="hero-shade"></div>
    <div class="brand"><span class="brand-mark"></span><span class="brand-name">Tavrin<br>Security Services Ltd</span></div>
    <div class="enquire">Enquire Now</div>
    <ul class="nav">
      <li class="active">Home</li>
      <li>About Tavrin</li>
      <li>Security Guards</li>
      <li>Security Patrols</li>
      <li>Tavrin Services</li>
      <li>Contact Us</li>
    </ul>
    <div class="slider-dots"><span class="on"></span><span></span></div>
  </header>

  <section class="services">
    <article class="service" style="left:32px">
      <div class="service-head">Tavrin Guard Service</div>
      <div class="service-avatar" role="img" aria-label="Guard avatar icon"></div>
      <p>Loremipsum Loremipsum Loremipsum Loremipsum Loremipsum</p>
      <p>Loremipsum Loremipsum Loremipsum Loremipsum Loremipsum</p>
      <span class="readmore">Readmore</span>
    </article>
    <article class="service" style="left:332px">
      <div class="service-head">Security Systems</div>
      <div class="service-avatar" role="img" aria-label="Guard avatar icon"></div>
      <p>Loremipsum Loremipsum Loremipsum Loremipsum Loremipsum</p>
      <p>Loremipsum Loremipsum Loremipsum Loremipsum Loremipsum</p>
      <span class="readmore">Readmore</span>
    </article>
    <article class="service" style="left:635px">
      <div class="service-head">Tavrin Guard Service</div>
      <div class="service-avatar" role="img" aria-label="Guard avatar icon"></div>
      <p>Loremipsum Loremipsum Loremipsum Loremipsum Loremipsum</p>
      <p>Loremipsum Loremipsum Loremipsum Loremipsum Loremipsum</p>
      <span class="readmore">Readmore</span>
    </article>
  </section>

  <section class="welcome">
    <h1>Welcome To <strong>Tavrin</strong> Security</h1>
    <p>Loremipsum Loremipsum Loremipsum Loremipsum Loremipsum Loremipsum Loremipsum Loremipsum Loremipsum Loremipsum</p>
    <p>Loremipsum Loremipsum Loremipsum Loremipsum Loremipsum Loremipsum Loremipsum Loremipsum Loremipsum Loremipsum Loremipsum Loremipsum Loremipsum Loremipsum Loremipsum Loremipsum Loremipsum Loremipsum Loremipsum Loremipsum</p>
    <p>Loremipsum Loremipsum Loremipsum Loremipsum Loremipsum Loremipsum Loremipsum Loremipsum Loremipsum Loremipsum Loremipsum Loremipsum Loremipsum Loremipsum Loremipsum Loremipsum Loremipsum Loremipsum Loremipsum Loremipsum</p>
  </section>

  <aside class="updates">
    <div class="updates-tab">Latest Updates</div>
    <div class="news" style="top:54px"><h3>News # 1</h3><p>Loremipsum Loremipsum Loremipsum Loremipsum Loremipsum Loremipsum Loremipsum Loremipsum Loremipsum Loremipsum</p></div>
    <div class="news-rule" style="top:128px"></div>
    <div class="news" style="top:137px"><h3>News # 1</h3><p>Loremipsum Loremipsum Loremipsum Loremipsum Loremipsum Loremipsum Loremipsum Loremipsum Loremipsum Loremipsum</p></div>
    <div class="news-rule" style="top:212px"></div>
    <div class="news" style="top:221px"><h3>News # 1</h3><p>Loremipsum Loremipsum Loremipsum Loremipsum Loremipsum Loremipsum Loremipsum Loremipsum Loremipsum Loremipsum</p></div>
  </aside>

  <div class="partners-label">PARTNERS</div>
  <section class="partners">
    <svg style="position:absolute;left:16px;top:22px" width="28" height="26" viewBox="0 0 28 26" aria-hidden="true"><path d="M26 2 L6 13 L26 24" fill="none" stroke="#8a8a8a" stroke-width="6"/></svg>
    <div class="partner box" style="left:89px"></div>
    <div class="partner blade" style="left:205px"></div>
    <div class="partner box" style="left:325px"></div>
    <div class="partner blade" style="left:441px"></div>
    <svg style="position:absolute;left:560px;top:22px" width="28" height="26" viewBox="0 0 28 26" aria-hidden="true"><path d="M2 2 L22 13 L2 24" fill="none" stroke="#8a8a8a" stroke-width="6"/></svg>
  </section>

  <footer class="footer">
    <ul class="foot-col" style="left:32px"><li>Home</li><li>About</li><li>Services</li></ul>
    <ul class="foot-col" style="left:102px"><li>Terms &amp; Conditions</li><li>Tavrin Policy</li><li>Contact</li></ul>
    <div class="follow">Follow Us</div>
    <span class="social" style="left:781px"></span>
    <span class="social" style="left:812px"></span>
    <div class="copyright">copyright all rights reserved - 2014</div>
  </footer>

</div>
</body>
</html>
```